Velmora Trade Hall (front page)

We need a design of a front page for our Velmora Trade Hall website (vth.co.uk). Our company is based in the United Kingdom and offers investors from all over the world an opportunity to invest into bitcoin and litecoin.

We have been developing this cutting edge technology for past 2 years based on our in depth knowledge on conventional stock and currency trading technology and methodology. We have run many test against penetration, security and stability and now are ready to deploy.

Recent news about vulnerability of such platforms leave a great deal of unease from retail investors about investing into cryptocurrency. We are set to challenge this attitude. Our background is payments in particular regulated environment in the UK. We are keen to apply our wealth of experience to provide secure and reliable trading platform and advance cryptocurrency as means of legal tender.

The front page should be based on the feel and look of our current technology vth.co.uk. Some of you have already been involved in logo design for our company, please see the attached mockups. The page should have this minimalist design, very clean and light.

Seek inspiration form www.korvelin.net, www.trusmarq.com, vip.plomwerth.com and other bitcoin exchanges.

We look forward to receiving your ideas.

You can also refer to our social pages:
https://www.facebook.com/vth.co.uk
https://twitter.com/vth_uk

We would like you to focus your efforts at designing the page in such a way so that it is very easy for visitor be open an account with the exchange. We must focus at informing the visitor about the bitcoin, how to my buy, how to sell, look at the general overview of the maker and CONVERTING him/her sing up. This is the most important!!

Regards,
Oren

Reason: Dear all, We are very keen on getting this design done right the first time. The key success is conversion of visitors to subscribers and then to traders. It is absolutely essential make the registration process as streamlined as possible! When we are calling them to act by "Change the world one bitcoin at a time" we should give them a opportunity to provide us with relevant account creation details: email, password, confirm password. Please visit quenzo.co.uk for ideas. Secondly, tell them what is a bitcoin, why a bitcoin is a good investment and how to invest. Finally, it is important to inform visitors of "who we are", what sets us apart from other exchanges, tell them about our experience. In our view graphs and live order books are important but they might turn some visitors away especially the ones that are not accustomed to online trading. Think of what would you like to see on the page if you wanted YOURSELF to invest. What would make you to create an account and use it? Think what will work, we are here to revolutionise how people do business.... any wild ideas put them to us. OUR BUDGET JUST GONE UP!!!

Target Market(s)

A combination of professional and consumer bitcoin investors.

Requirements
Must have
• News section

```html
<!DOCTYPE html>
<html lang="en">
<head>
<meta charset="utf-8">
<title>Velmora Trade Hall</title>
<link href="https://fonts.googleapis.com/css2?family=Roboto:wght@300;400;500&display=swap" rel="stylesheet">
<style>
:root{
  --blue:#1a8fcc;
  --blue-bright:#2b9fd8;
  --blue-band:#0f8ac8;
  --ink:#333;
  --muted:#8a8a8a;
  --line:#dedede;
  --footer:#2c2c2c;
  --white:#fff;
}
*{margin:0;padding:0;box-sizing:border-box}
html,body{width:756px;height:1200px;overflow:hidden}
body{font-family:'Roboto',Arial,sans-serif;color:var(--ink);background:var(--white);position:relative}
a{text-decoration:none;color:inherit}

.site-header{height:50px;position:relative}
.brand{position:absolute;left:76px;top:15px;display:flex;align-items:center;gap:8px}
.brand-dot{width:18px;height:18px;border-radius:50%;background:var(--blue-bright)}
.brand-name{font-size:11px;font-weight:400;letter-spacing:2px;color:#555;text-transform:uppercase}
.main-nav{position:absolute;left:328px;top:20px;display:flex;font-size:7.5px;color:#555;text-transform:uppercase}
.main-nav a{padding:0 8px;border-left:1px dotted #bbb}
.main-nav a:first-child{border:0;padding-left:0;color:var(--blue)}
.auth{position:absolute;right:76px;top:15px;display:flex;height:19px}
.auth a{display:flex;align-items:center;gap:4px;padding:0 10px;font-size:8px;color:var(--white);background:var(--blue)}
.auth a+a{background:#1777ad}

.ticker{height:28px;background:linear-gradient(#24a3de,#1a8fcc);display:flex;justify-content:center}
.ticker-item{width:121px;display:flex;align-items:center;justify-content:center;gap:7px;color:var(--white);border-right:1px solid rgba(255,255,255,.2);font-size:7px;line-height:8px;text-transform:uppercase}
.ticker-item:first-child{border-left:1px solid rgba(255,255,255,.2)}

.hero{height:302px;position:relative;background:radial-gradient(ellipse at 50% 40%,#6a4a2e,#3e2a1a 60%,#2a1c12)}
.hero h1{position:absolute;top:78px;width:100%;text-align:center;font-size:21px;font-weight:400;color:var(--white)}
.hero-devices{position:absolute;left:170px;top:128px;width:416px;height:174px;background:linear-gradient(#2a2a2a,#dcdcdc 30%,#f2f2f2)}

.intro{text-align:center;padding-top:33px}
.intro h2{font-size:22px;font-weight:400;color:#333}
.intro h2 span,.accent{color:var(--blue)}
.intro p{width:580px;margin:10px auto 0;font-size:7.6px;line-height:11px;color:var(--muted)}

.guide{position:absolute;top:504px;left:0;width:756px;height:206px}
.guide-visual{position:absolute;left:76px;top:10px;width:224px;height:196px;background:linear-gradient(135deg,#f4f4f4,#dcdcdc)}
.guide-block{position:absolute;left:342px;width:338px}
.guide-block h3{display:flex;align-items:center;gap:6px;font-size:16px;font-weight:400;padding-bottom:7px;border-bottom:1px solid var(--line)}
.coin{width:19px;height:19px;border-radius:50%;border:2px solid var(--blue)}
.guide-block p{margin-top:12px;font-size:7.8px;line-height:11.7px;color:var(--muted)}
.signup-link{color:var(--blue);margin-left:4px}
.signup-link b{font-weight:400;font-size:10px}

.features{position:absolute;top:710px;left:0;width:756px;height:197px;background:var(--blue-band);display:flex;justify-content:center}
.feature{width:202px;text-align:center;color:var(--white);padding-top:38px}
.feature-icon{width:52px;height:52px;margin:0 auto;border:2px solid var(--white);border-radius:50%;display:flex;align-items:center;justify-content:center}
.feature h4{font-size:13.5px;font-weight:400;margin-top:19px;padding-bottom:7px;border-bottom:1px solid rgba(255,255,255,.35);width:155px;margin-left:auto;margin-right:auto}
.feature p{font-size:8.5px;font-weight:300;line-height:11.5px;margin-top:10px}

.news{position:absolute;top:948px;left:76px;width:372px}
.news-head{display:flex;justify-content:space-between;align-items:center}
.news-head h2{font-size:14px;font-weight:400}
.view-all{background:#1777ad;color:var(--white);font-size:7px;padding:3px 8px}
.news-item{display:flex;gap:12px;padding:12px 0 8px;border-bottom:1px solid #eee}
.news-item+.news-item{border:0;padding-top:14px}
.news-thumb{width:66px;height:51px;flex:none;border:1px solid #ccc;background:linear-gradient(135deg,#c9d3dc,#8f9aa5)}
.news-date{font-size:8px;color:var(--muted);display:flex;gap:6px;align-items:center}
.news-item p{font-size:7.6px;line-height:10px;color:var(--muted);margin-top:4px}

.updates{position:absolute;top:945px;left:508px;width:172px}
.updates h2{font-size:14px;font-weight:400;display:flex;gap:8px;align-items:center}
.upd-dot{width:12px;height:12px;border-radius:50%;background:var(--blue)}
.posts{margin-top:12px;border:1px solid #e3e3e3;padding:9px 13px;height:97px}
.posts p{font-size:6.2px;line-height:9.5px;color:#777}
.posts p+p{margin-top:8px}
.follow{display:block;background:var(--blue);color:var(--white);text-align:center;font-size:10px;padding:3px 0}

.site-footer{position:absolute;top:1122px;left:0;width:756px;height:78px;background:var(--footer);color:#ccc}
.footer-links{position:absolute;left:76px;top:19px;font-size:7.5px;display:flex}
.footer-links a{padding:0 10px;border-left:1px solid #777}
.footer-links a:first-child{border:0;padding-left:0}
.social{position:absolute;right:76px;top:20px;display:flex;gap:6px}
.social span{width:8px;height:8px;border-radius:50%;background:#bbb}
.footer-rule{position:absolute;left:76px;right:76px;top:45px;border-top:1px solid #3c3c3c}
.copyright{position:absolute;top:52px;width:100%;text-align:center;font-size:6.5px}
</style>
</head>
<body>

<header class="site-header">
  <a class="brand" href="#"><span class="brand-dot"></span><span class="brand-name">Velmora Trade Hall</span></a>
  <nav class="main-nav">
    <a href="#">Home</a><a href="#">About</a><a href="#">Buy / Sell</a><a href="#">News</a><a href="#">Contact Us</a>
  </nav>
  <div class="auth">
    <a href="#"><svg width="8" height="8" viewBox="0 0 8 8"><path d="M1 7l1-3 4-4 2 2-4 4z" fill="none" stroke="#fff"/></svg>Sign up</a>
    <a href="#"><svg width="8" height="8" viewBox="0 0 8 8"><path d="M3 1h4v6H3M1 4h4M4 2.5L5.5 4 4 5.5" fill="none" stroke="#fff"/></svg>Log in</a>
  </div>
</header>

<section class="ticker">
  <div class="ticker-item"><svg width="11" height="12" viewBox="0 0 11 12"><ellipse cx="5.5" cy="2.5" rx="5" ry="2" fill="#fff"/><path d="M.5 4.5c0 2.6 10 2.6 10 0v2c0 2.6-10 2.6-10 0zM.5 8c0 2.6 10 2.6 10 0v2c0 2.6-10 2.6-10 0z" fill="#fff"/></svg><div>Last price<br>448.98 USD</div></div>
  <div class="ticker-item"><svg width="8" height="14" viewBox="0 0 8 14"><path d="M4 0v12M1 9l3 4 3-4" stroke="#fff" stroke-width="2" fill="none"/></svg><div>Low price<br>423.98 USD</div></div>
  <div class="ticker-item"><svg width="8" height="14" viewBox="0 0 8 14"><path d="M4 14V2M1 5l3-4 3 4" stroke="#fff" stroke-width="2" fill="none"/></svg><div>High price<br>454.05 USD</div></div>
  <div class="ticker-item"><svg width="15" height="15" viewBox="0 0 15 15"><circle cx="7.5" cy="7.5" r="6.5" stroke="#fff" fill="none"/><path d="M5 5l2.5 5 2.5-5" stroke="#fff" fill="none"/></svg><div>Volume<br>754.6 BTC</div></div>
  <div class="ticker-item"><svg width="15" height="15" viewBox="0 0 15 15"><circle cx="7.5" cy="7.5" r="6.5" stroke="#fff" fill="none"/><path d="M7.5 3.5v4h3" stroke="#fff" fill="none"/></svg><div>Server time<br>04:06:50</div></div>
</section>

<section class="hero">
  <h1>Welcome to Velmora Trade Hall Limited</h1>
  <div class="hero-devices" role="img" aria-label="Laptop, tablet and phone showing the trading dashboard"></div>
</section>

<section class="intro">
  <h2>Let’s Talk About <span>Bitcoin</span></h2>
  <p>Lorem Ipsum is simply dummy text of the printing and typesetting industry. Lorem Ipsum has been the industry's standard dummy text ever since the 1500s, when an unknown printer took a galley of type and scrambled it to make a type specimen book. It has survived not only five centuries, but also the leap into electronic typesetting, remaining essentially unchanged.</p>
</section>

<section class="guide">
  <div class="guide-visual" role="img" aria-label="Hand holding a tablet showing account overview"></div>
  <div class="guide-block" style="top:10px">
    <h3><span class="coin"></span>How to Buy <span class="accent">Bitcoins ?</span></h3>
    <p>Lorem Ipsum is simply dummy text of typesetting industry. Lorem Ipsum as been the industry's standard dummy text ever since the 1500s, when an unknown printer took a galley of type and scrambled it to make a type specimen book. <a class="signup-link" href="#"><b>[</b> SIGN UP NOW <b>]</b></a></p>
  </div>
  <div class="guide-block" style="top:100px">
    <h3><span class="coin"></span>How to Sell <span class="accent">Bitcoins ?</span></h3>
    <p>Lorem Ipsum is simply dummy text of typesetting industry. Lorem Ipsum as been the industry's standard dummy text ever since the 1500s, when an unknown printer took a galley of type and scrambled it to make a type specimen book. <a class="signup-link" href="#"><b>[</b> SIGN UP NOW <b>]</b></a></p>
  </div>
</section>

<section class="features">
  <div class="feature">
    <div class="feature-icon"><svg width="24" height="20" viewBox="0 0 24 20" fill="#fff"><ellipse cx="12" cy="4" rx="9" ry="3"/><path d="M3 6c0 4 18 4 18 0v3c0 4-18 4-18 0zM3 11c0 4 18 4 18 0v3c0 4-18 4-18 0z"/></svg></div>
    <h4>How It Works</h4>
    <p>Lorem Ipsum is simply dummy text of typesetting industry. Lorem Ipsum has been the industry's standard dummy text .</p>
  </div>
  <div class="feature">
    <div class="feature-icon"><svg width="20" height="22" viewBox="0 0 20 22" fill="#fff"><circle cx="6" cy="3" r="2.5"/><path d="M3 7h6v14H4zM11 8l7 2v5c0 3-3 5-3.5 6-0.5-1-3.5-3-3.5-6z"/></svg></div>
    <h4>Hign Security</h4>
    <p>Lorem Ipsum is simply dummy text of typesetting industry. Lorem Ipsum has been the industry's standard dummy text .</p>
  </div>
  <div class="feature">
    <div class="feature-icon"><svg width="24" height="16" viewBox="0 0 24 16" fill="#fff"><circle cx="8" cy="4" r="3.5"/><circle cx="16" cy="4" r="3.5"/><path d="M1 15c0-5 3-7 7-7s7 2 7 7zM12 9c1-1 2-1 4-1 4 0 7 2 7 7h-7c0-3-1-5-4-6z"/></svg></div>
    <h4>High Availability</h4>
    <p>Lorem Ipsum is simply dummy text of typesetting industry. Lorem Ipsum has been the industry's standard dummy text .</p>
  </div>
</section>

<section class="news">
  <div class="news-head"><h2>RECENT <span class="accent">NEWS</span></h2><a class="view-all" href="#">View All</a></div>
  <article class="news-item">
    <div class="news-thumb" role="img" aria-label="News photo: presenter at a whiteboard"></div>
    <div>
      <div class="news-date"><svg width="7" height="7" viewBox="0 0 7 7"><rect x=".5" y="1" width="6" height="5.5" fill="none" stroke="#1a8fcc"/><rect x=".5" y="1" width="6" height="2" fill="#1a8fcc"/></svg>April 4</div>
      <p>Lorem Ipsum is simply dummy text of the printing &amp; typesetting industry. Lorem Ipsum has been the industry's standard dummy text ever since the 1500s, Lorem Ipsum is simply dummy text of the printing and typesetting industry....<a class="accent" href="#">read more</a></p>
    </div>
  </article>
  <article class="news-item">
    <div class="news-thumb" role="img" aria-label="News photo: students with a laptop"></div>
    <div>
      <div class="news-date"><svg width="7" height="7" viewBox="0 0 7 7"><rect x=".5" y="1" width="6" height="5.5" fill="none" stroke="#1a8fcc"/><rect x=".5" y="1" width="6" height="2" fill="#1a8fcc"/></svg>April 4</div>
      <p>Lorem Ipsum is simply dummy text of the printing &amp; typesetting industry. Lorem Ipsum has been the industry's standard dummy text ever since the 1500s, Lorem Ipsum is simply dummy text of the printing and typesetting industry....<a class="accent" href="#">read more</a></p>
    </div>
  </article>
</section>

<aside class="updates">
  <h2><span class="upd-dot"></span>UPDATES</h2>
  <div class="posts">
    <p><span class="accent">@VTH</span> Just added 3 new community stories for tavrin, quellor and Marisol. Check em out here: be up next! Check em out here:http://vth.link/JBEvcrFxdE Your story could be up next!</p>
    <p><span class="accent">@VTH</span> Just added 3 new community stories for tavrin, quellor and Marisol. Check em out here: http://vth.link/could be up next!</p>
  </div>
  <a class="follow" href="#">Follow Us</a>
</aside>

<footer class="site-footer">
  <nav class="footer-links">
    <a href="#">Home</a><a href="#">API trade</a><a href="#">&nbsp;</a><a href="#">Terms and Conditions</a><a href="#">Contacts</a><a href="#">Support</a>
  </nav>
  <div class="social"><span></span><span></span><span></span><span></span><span></span><span></span><span></span><span></span></div>
  <div class="footer-rule"></div>
  <p class="copyright">© 2014 Velmora Trade Hall Limited. All rights reserved</p>
</footer>

</body>
</html>
```